Restaurant needs promotional material

We need a design for a "free welcome cocktail on your next visit" flyer. The flyer must have a black background and be contemporary. Our logo is the name of the restaurant which is "Amber Nook" in edwardian script font with italic selected.

There must be a section for terms and conditions, which are:
1 free cocktail for every main course ordered from our evening menu over the value of 9.95€ (not including taxes). The number of free cocktails cannot exceed the number of main courses ordered from your previous visit. This offer is only valid when you present both this flyer and your receipt from your previous visit. This offer does not include ice cream cocktails. This offer cannot be used in conjunction with any other offer or promotion. Limit 1 free cocktail per person. We reserve the right to final interpretation of this offer and can cancel the offer at any time.

A space must also be left where we can write a "valid until" date.

The uploaded photos are a picture of our cocktail menu and the publicity we are currently running, so you can get a feel for your design.

Thanks

Industry/Entity Type

Restaurant

Colors
000000

Requirements
Must have
• Also included in the flyer is the text " Please present this flyer along with your bill from your previous visit upon arrival.
• Pictures of cocktails!

```html
<!DOCTYPE html>
<html lang="en">
<head>
<meta charset="utf-8">
<title>Amber Nook – Free Welcome Cocktail Flyer</title>
<link rel="stylesheet" href="https://fonts.googleapis.com/css2?family=Marcellus&family=Advent+Pro:wght@300;400&display=swap">
<style>
  :root {
    --flyer-black: #000000;
    --brand-pink: #e0489a;
    --accent-magenta: #c2186f;
    --accent-blue: #2aa4c8;
    --text-light: #f2f2f2;
    --text-muted: #c9c9c9;
    --field-grey: #939598;
    --field-text: #1a1a1a;
  }
  * { margin: 0; padding: 0; box-sizing: border-box; }
  html, body {
    width: 921px;
    height: 1200px;
    overflow: hidden;
    background: var(--flyer-black);
  }
  .flyer {
    position: relative;
    width: 921px;
    height: 1200px;
    background: var(--flyer-black);
    color: var(--text-light);
    overflow: hidden;
  }
  .splash-top-left,
  .splash-top-right,
  .cocktail-photo {
    position: absolute;
  }
  .splash-top-left {
    left: 0; top: 0; width: 260px; height: 330px;
    background: radial-gradient(ellipse at 20% 30%, rgba(194,24,111,0.55), rgba(120,20,80,0.15) 55%, transparent 75%);
  }
  .splash-top-right {
    right: 0; top: 0; width: 320px; height: 400px;
    background: radial-gradient(ellipse at 70% 35%, rgba(42,164,200,0.35), rgba(150,60,170,0.25) 45%, transparent 75%);
  }
  .cocktail-photo {
    left: 0; top: 380px; width: 921px; height: 440px;
    background:
      radial-gradient(ellipse 260px 200px at 26% 45%, rgba(214,36,138,0.85), rgba(120,16,80,0.35) 60%, transparent 80%),
      radial-gradient(ellipse 260px 220px at 78% 48%, rgba(42,164,200,0.85), rgba(20,90,120,0.35) 60%, transparent 80%),
      radial-gradient(ellipse 120px 90px at 52% 30%, rgba(230,230,230,0.35), transparent 80%);
  }
  .brand-name {
    position: absolute;
    left: 0; right: 0; top: 150px;
    text-align: center;
    font-family: "Marcellus", serif;
    font-weight: 400;
    font-size: 104px;
    line-height: 1;
    color: var(--brand-pink);
    letter-spacing: 1px;
  }
  .offer-headline {
    position: absolute;
    left: 0; right: 0; top: 265px;
    text-align: center;
    font-family: "Marcellus", serif;
    font-size: 33px;
    letter-spacing: 2px;
    color: var(--text-light);
  }
  .offer-subline {
    position: absolute;
    left: 0; right: 0; top: 306px;
    text-align: center;
    font-family: "Marcellus", serif;
    font-size: 29px;
    color: var(--text-light);
  }
  .divider {
    position: absolute;
    left: 139px; top: 818px;
    width: 641px; height: 3px;
    background: linear-gradient(90deg, transparent, var(--accent-magenta) 20%, var(--accent-magenta) 80%, transparent);
  }
  .conditions-title {
    position: absolute;
    left: 0; right: 0; top: 851px;
    text-align: center;
    font-family: "Advent Pro", sans-serif;
    font-weight: 400;
    font-size: 16px;
    letter-spacing: 0.5px;
    color: var(--text-muted);
  }
  .conditions-text {
    position: absolute;
    left: 56px; width: 812px; top: 884px;
    text-align: center;
    font-family: "Advent Pro", sans-serif;
    font-weight: 300;
    font-size: 18.5px;
    line-height: 23px;
    color: var(--text-muted);
  }
  .present-note {
    position: absolute;
    left: 0; right: 0; top: 1050px;
    text-align: center;
    font-family: "Advent Pro", sans-serif;
    font-weight: 400;
    font-size: 20px;
    color: var(--brand-pink);
  }
  .valid-until {
    position: absolute;
    left: 295px; top: 1107px;
    width: 329px; height: 26px;
    background: var(--field-grey);
    padding: 1px 4px;
    font-family: "Advent Pro", sans-serif;
    font-weight: 400;
    font-size: 19px;
    line-height: 24px;
    color: var(--field-text);
  }
</style>
</head>
<body>
  <main class="flyer">
    <div class="splash-top-left" role="img" aria-label="Magenta liquid splash with droplets"></div>
    <div class="splash-top-right" role="img" aria-label="Blue and purple liquid splash with droplets"></div>

    <h1 class="brand-name">Amber Nook</h1>
    <p class="offer-headline">FREE WELCOME COCKTAIL</p>
    <p class="offer-subline">on your next visit</p>

    <div class="cocktail-photo" role="img" aria-label="Photo of a pink and a blue martini glass clinking with liquid splashing between them"></div>

    <div class="divider"></div>

    <h2 class="conditions-title">CONDITIONS</h2>
    <p class="conditions-text">1 free cocktail for every main course ordered from our evening menu over the value of 9.95€ (not including taxes). The number of free cocktails cannot exceed the number of main courses ordered from your previous visit. This offer is only valid when you present both this flyer and your receipt from your previous visit. This offer does not include ice cream cocktails. This offer cannot be used in conjunction with any other offer or promotion. Limit 1 free cocktail per person. We reserve the right to final interpretation of this offer and can cancel the offer at any time.</p>

    <p class="present-note">Please present this flyer along with your bill from your previous visit upon arrival.</p>

    <div class="valid-until">valid until:</div>
  </main>
</body>
</html>
```